Brickline Gains Online Redesign

The company needs a new online presence built that better represents who we are and what we do. Our online presence needs to be optimised for both PC, tablet and Phone usage.

Our existing site; www.bricklinegains.com.au - this page currently forwards to one of our sales pages.
The entire site needs to be redesigned along with the sales pages /workshop and /faststart

Here are our competition:
https://www.coraltemsby.com/
http://quorvahomeschooling.com.au/property-education-experts/coral-temsby/
http://harrietvolonsky.com.au/
www.refitforyield.com.au/
http://fullmanualtorefurb.com.au/

Target Market(s)

40-55 Husband and Wife with children that are busy profesionals with a family income of 150-300k PA with 2-3 kids

Industry/Entity Type

Education

Number of Pages Required

5+ page

Font styles to use
Sans Serif
Script

Colors

Designer to choose colors to be used in the design.

Requirements
Must have
• Main Page
• Events Page
• Media Page
• Past Projects
• Blog - plesae design a template blog; both individual blogs and library (i like this http://bram.blog/)
• eBooks page
• Shopping Cart - buy eBooks, eBook Packs and courses
• eBook download page for each eBook
• Testimonials
• Event Sales Page
• 2 hr Event - currently www.bricklinegains.com.au/workshop & /faststart & /faststartv
Nice to have
• A few different options for sales landing pages to sell the 2 hr event
• A few different blog templates - video, text, infographic etc
• The business is a Property Educatiom, Mentoring and Consulting Company
Should not have
• This is not a real estate sales business

```html
<!DOCTYPE html>
<html lang="en">
<head>
<meta charset="utf-8">
<title>Brickline Gains — Property Education</title>
<link href="https://fonts.googleapis.com/css2?family=Montserrat:ital,wght@0,600;0,700;0,800;1,800&family=Open+Sans:ital,wght@0,400;0,600;0,700;1,400;1,600&display=swap" rel="stylesheet">
<style>
:root{
  --navy:#0d2257;
  --navy-deep:#081843;
  --orange:#f0831e;
  --teal:#1fb79b;
  --blue:#2d74c4;
  --band-blue:#1e3f8e;
  --red:#d3141c;
  --ink:#222831;
  --muted:#555b66;
  --grey:#ececec;
  --grey-2:#e2e2e2;
  --charcoal:#2b2b2b;
  --charcoal-deep:#1d1d1d;
  --white:#ffffff;
}
*{box-sizing:border-box;margin:0;padding:0}
html,body{width:1200px;height:4036px;overflow:hidden}
body{position:relative;background:var(--white);font-family:"Open Sans",Arial,sans-serif;color:var(--ink);font-size:13px;line-height:1.45}
.block{position:absolute;left:0;width:1200px}
.abs{position:absolute}
h1,h2,h3,h4{font-family:"Montserrat",Arial,sans-serif}
.btn{display:inline-flex;align-items:center;justify-content:center;gap:10px;background:var(--teal);color:var(--white);font-family:"Montserrat",Arial,sans-serif;font-weight:700;text-decoration:none;border-radius:4px;box-shadow:0 4px 0 #14866f}
.btn-small{background:var(--blue);color:#fff;font-size:11px;font-weight:700;font-family:"Montserrat",Arial,sans-serif;padding:4px 14px;border-radius:2px}
.read-more{color:var(--blue);font-weight:700;font-size:12px;text-transform:uppercase}
.ph{display:block}

/* header */
.site-header{top:0;height:102px;background:#fff}
.logo{left:92px;top:24px;display:flex;align-items:center;gap:12px}
.logo-mark{width:36px;height:36px;background:var(--navy)}
.logo-name{font-family:"Montserrat",Arial,sans-serif;font-weight:800;font-size:26px;color:var(--navy);line-height:1}
.ask{left:715px;top:28px;display:flex;align-items:center;gap:12px}
.ask small{display:block;font-size:14px;color:var(--ink)}
.ask strong{display:block;font-family:"Montserrat",sans-serif;font-size:25px;font-weight:800;color:var(--ink);line-height:1}
.header-cta{left:925px;top:0;width:200px;height:100px;background:var(--teal);color:#fff;font-family:"Montserrat",sans-serif;font-weight:800;font-size:24px;line-height:1.05;display:flex;align-items:center;justify-content:center;text-align:center}
.main-nav{top:102px;height:44px;background:var(--navy-deep);display:flex;justify-content:center}
.main-nav a{color:#fff;text-decoration:none;font-size:15px;font-family:"Montserrat",sans-serif;font-weight:600;padding:0 25px;line-height:44px}
.main-nav a.active{background:#243a75}

/* hero */
.hero{top:146px;height:560px;background:linear-gradient(180deg,#3b3f7a 0%,#6a6aa6 35%,#a47d7a 62%,#3a5f83 78%,#27506e 100%)}
.hero-panel{left:230px;top:172px;width:580px;height:300px;background:var(--orange);clip-path:polygon(8% 0,100% 0,100% 100%,0 100%)}
.hero-portrait{left:81px;top:162px;width:190px;height:190px;border-radius:50%;background:linear-gradient(160deg,#dfe4ea,#8a97a8);border:5px solid #fff}
.hero-copy{left:290px;top:195px;width:500px;color:#fff}
.hero-copy h1{font-size:34px;font-weight:800;font-style:italic;line-height:1.08;text-transform:uppercase}
.hero-copy p{font-size:16px;margin-top:8px}
.hero-copy .btn{margin-top:20px;width:325px;height:50px;font-size:18px}
.secure{font-size:12px;font-style:italic;margin-top:14px;padding-left:35px}

/* as seen */
.as-seen{top:706px;height:135px;background:var(--grey-2);text-align:center}
.as-seen h4{font-family:"Open Sans",sans-serif;font-size:13px;font-weight:700;margin-top:16px;color:var(--ink)}
.badges{display:flex;justify-content:center;gap:30px;margin-top:22px}
.badges span{width:140px;height:48px;background:#c4c6ca;border-radius:4px}

/* about */
.about{top:841px;height:343px;background:#fff}
.about-panel{left:545px;top:0;width:655px;height:343px;background:var(--navy)}
.about-video{left:73px;top:28px;width:492px;height:275px;background:linear-gradient(180deg,#8fb7d8,#e2e8ec 55%,#7c8a94)}
.play{left:285px;top:147px;width:70px;height:50px;border-radius:10px;background:rgba(40,120,200,.85)}
.video-bar{left:73px;top:279px;width:492px;height:24px;background:rgba(10,25,60,.8);color:#fff;font-size:12px;padding:4px 10px}
.about-copy{left:585px;top:28px;width:540px;color:#fff}
.about-copy h2{font-size:26px;font-weight:700}
.about-copy p{font-size:12.5px;line-height:1.6;margin-top:10px;color:#e6ebf5}
.about-copy .btn-small{display:inline-block;margin-top:12px;background:var(--teal)}

/* events */
.events{top:1184px;height:497px;background:linear-gradient(180deg,#3d3d3d 0 160px,var(--grey) 160px)}
.events-card{left:73px;top:32px;width:1052px;height:433px;background:var(--orange);border:3px solid #fff}
.events-map{left:94px;top:40px;width:492px;height:422px;background:linear-gradient(135deg,#e6eadc,#c7dcb0 45%,#a9cbe6)}
.events-copy{left:610px;top:52px;width:500px;color:#fff}
.events-copy h2{font-size:27px;font-weight:700}
.events-copy h3{font-size:18px;font-weight:700;margin-top:10px;line-height:1.25}
.events-copy p{font-size:13px;margin-top:10px;line-height:1.5}
.events-copy h4{text-align:center;font-family:"Open Sans",sans-serif;font-weight:600;font-size:14px;margin-top:14px}
.event-table{display:grid;grid-template-columns:150px 110px 1fr;margin-top:10px;font-size:13px;row-gap:2px}
.event-table b{font-size:14px}
.events-copy .btn{margin:22px 0 0 80px;width:330px;height:48px;font-size:17px}
.events-copy .secure{padding-left:95px}

/* instructors */
.instructors{top:1681px;height:471px}
.section-title{display:flex;align-items:center;gap:20px;justify-content:center;padding:30px 73px 0}
.section-title::before,.section-title::after{content:"";flex:1;height:10px;background:#e3e3e3}
.section-title h2{font-size:27px;font-weight:700;letter-spacing:1px}
.instructor{top:81px;width:506px;height:242px;background:var(--grey)}
.instructor .avatar{left:20px;top:20px;width:110px;height:110px;border-radius:50%;background:linear-gradient(160deg,#e8ecf0,#9aa5b2);border:4px solid #fff}
.instructor .txt{left:150px;top:18px;width:335px}
.instructor h3{font-size:20px;font-weight:700}
.instructor p{font-size:12px;color:var(--muted);margin-top:6px;line-height:1.55}
.instructor .read-more{display:block;margin-top:8px;font-size:11px}
.book-strip{text-align:center}
.book-strip small{display:block;font-size:11px;font-weight:700;margin-bottom:6px}
.book-strip .btn{width:200px;height:46px;font-size:18px}

/* blog + testimonials */
.blogtest{top:2179px;height:500px}
.col-head{display:flex;justify-content:space-between;align-items:center}
.col-head h2{font-size:26px;font-weight:700}
.blog-card{top:89px;width:244px}
.blog-img{width:244px;height:134px;background:linear-gradient(180deg,#c9d3dc,#eef1f3 50%,#9aa6b1);position:relative}
.blog-card h3{font-family:"Open Sans",sans-serif;font-size:14px;font-weight:700;margin-top:14px;line-height:1.35}
.blog-card .meta{font-size:11px;color:var(--muted);margin-top:6px}
.blog-card p{font-size:12px;color:var(--muted);margin-top:8px;line-height:1.5}
.quote{left:613px;width:512px;background:var(--navy);color:#fff;font-style:italic;font-size:13.5px;line-height:1.5;padding:20px 40px 22px 40px}
.quote .qm{position:absolute;font-family:"Montserrat",sans-serif;font-style:normal;font-weight:800;font-size:40px;line-height:1;color:#fff}
.cite{left:623px;font-size:12px;color:var(--muted);font-style:italic}

/* success stories */
.success{top:2698px;height:471px;background:var(--band-blue)}
.success h2{color:#fff;text-align:center;font-size:26px;font-weight:700;padding-top:24px}
.story{top:92px;width:336px;height:340px;background:#fff;padding:14px 14px 0}
.story h3{text-align:center;font-size:15px;font-weight:600;color:var(--ink)}
.story-photo{margin-top:12px;height:200px;background:linear-gradient(180deg,#9cc4e8 0 45%,#b99a7a 45% 70%,#7fa05a 70%)}
.story-figs{display:flex;justify-content:space-between;margin-top:10px}
.story-figs .bs{font-size:14px;font-weight:700;color:var(--blue);line-height:1.35}
.story-figs .bs span{color:var(--navy)}
.profit{width:130px;height:64px;background:var(--red);color:#fff;text-align:center;font-family:"Montserrat",sans-serif;font-weight:800;font-size:22px;line-height:1.1;padding-top:8px}
.profit small{display:block;font-size:14px}
.arrow{top:215px;width:40px;height:50px}

/* faq + ebooks */
.faqbooks{top:3188px;height:380px}
.faq-q{left:73px;width:513px;height:40px;background:var(--grey-2);font-weight:700;font-size:14px;padding:9px 16px;display:flex;justify-content:space-between}
.faq-q .tog{width:40px;height:40px;margin:-9px -16px 0 0;background:#b7b9bd;color:#fff;font-size:28px;line-height:40px;text-align:center;font-weight:400}
.faq-a{left:73px;width:513px;font-size:12.5px;color:var(--muted);line-height:1.55}
.faq-a a{color:var(--blue);font-weight:600;text-decoration:none}
.ebook{top:72px;width:155px}
.ebook-cover{height:215px;border:1px solid #ddd;padding:8px}
.ebook-cover div{height:100%}
.price{text-align:center;color:var(--red);font-weight:700;font-size:15px;margin-top:8px}

/* footer */
.site-footer{top:3699px;height:255px;background:var(--charcoal);color:#fff}
.site-footer h4{font-size:15px;font-weight:700;margin-bottom:8px}
.site-footer ul{list-style:none;font-size:13px;line-height:1.5;color:#e2e2e2}
.contact-list{font-size:13px;color:#e2e2e2;line-height:1.45}
.social{display:flex;gap:8px}
.social span{width:34px;height:34px;border:2px solid #fff;border-radius:50%}
.news p{font-size:12.5px;color:#e2e2e2;line-height:1.45}
.news .field{width:245px;height:30px;background:#fff;margin-top:8px;color:#888;font-size:12px;padding:6px 10px}
.news .sign{width:245px;height:34px;background:var(--teal);margin-top:8px;text-align:center;font-family:"Montserrat",sans-serif;font-weight:700;font-size:15px;line-height:34px}
.copyright{top:3954px;height:82px;background:var(--charcoal-deep);color:#e2e2e2;text-align:center;font-size:12.5px;padding-top:20px;line-height:1.55}
</style>
</head>
<body>

<header class="block site-header">
  <div class="abs logo"><span class="logo-mark"></span><span class="logo-name">Brickline Gains</span></div>
  <div class="abs ask">
    <svg width="36" height="36" viewBox="0 0 24 24" aria-hidden="true"><path fill="#222831" d="M6.6 10.8a15 15 0 006.6 6.6l2.2-2.2c.3-.3.7-.4 1-.2 1.1.4 2.3.6 3.6.6.6 0 1 .4 1 1V20c0 .6-.4 1-1 1A17 17 0 013 4c0-.6.4-1 1-1h3.5c.6 0 1 .4 1 1 0 1.3.2 2.5.6 3.6.1.3 0 .7-.2 1z"/></svg>
    <div><small>Ask A Question:</small><strong>1300 555 014</strong></div>
  </div>
  <a class="abs header-cta">BOOK MY<br>SEAT NOW!</a>
</header>

<nav class="block main-nav">
  <a class="active">HOME</a><a>OUR EVENTS</a><a>PAST PROJECTS</a><a>MEDIA EBOOKS</a><a>TESTIMONIALS</a><a>BLOG</a><a>CONTACT US</a>
</nav>

<section class="block hero" role="img" aria-label="Renovated two-storey home with lit pool at dusk">
  <div class="abs hero-panel"></div>
  <div class="abs hero-portrait" role="img" aria-label="Portrait of the two workshop presenters"></div>
  <div class="abs hero-copy">
    <h1>Learn how to make a living as a professional property rennovator!</h1>
    <p>2 Hour Fast Paced Workshop in Sydney</p>
    <a class="btn">
      <svg width="22" height="20" viewBox="0 0 24 22" aria-hidden="true"><path fill="#fff" d="M1 1h4l3 12h12l3-9H7" stroke="#fff" stroke-width="2" fill-opacity="0"/><circle cx="10" cy="18" r="2" fill="#fff"/><circle cx="18" cy="18" r="2" fill="#fff"/></svg>
      YES - BOOK MY SEAT NOW
    </a>
    <div class="secure">**Secure Booking - Your Details are Safe!**</div>
  </div>
</section>

<section class="block as-seen">
  <h4>AS SEEN ON</h4>
  <div class="badges"><span></span><span></span><span></span><span></span><span></span><span></span></div>
</section>

<section class="block about">
  <div class="abs about-panel"></div>
  <div class="abs about-video" role="img" aria-label="Video still of presenter speaking beside a pool"></div>
  <div class="abs play"><svg width="70" height="50" viewBox="0 0 70 50" aria-hidden="true"><path d="M28 15l16 10-16 10z" fill="#fff"/></svg></div>
  <div class="abs video-bar">▶ &nbsp;5:50</div>
  <div class="abs about-copy">
    <h2>ABOUT BRICKLINE GAINS</h2>
    <p>Learn how to significantly increase your income and live an extraordinary life in this ground up fundamentals workshop. You will learn how to select, finance and make the correct choices in renovating a property as well as the terminology used in the industry. You will also be introduced to negotiating with both agents and finance institutions along with a deep-dive look at some real world case studies. This workshop is ideal for those who seek alternative paths to true financial freedom and is perfect for people at any stage of their life - from buying their first home to looking at investing in property for their future.</p>
    <span class="btn-small">READ MORE</span>
  </div>
</section>

<section class="block events">
  <div class="abs events-card"></div>
  <div class="abs events-map" role="img" aria-label="Street map of Parramatta with the venue marked"></div>
  <div class="abs events-copy">
    <h2>OUR EVENTS</h2>
    <h3>RENOVATING PROPERTY FOR PROFIT WORKSHOP</h3>
    <p>Book your seat now for only $29 to attend this LIVE Training Event so we can show you how we've Successfully Renovated 20 Properties for Profit in the last 3 years alone... <b>and make more money in 12 weeks Renovating Property than most people make in 12 months in a job!</b></p>
    <h4>Event Details</h4>
    <div class="event-table">
      <b>DATE</b><b>TIME</b><b>LOCATION</b>
      <span>Tuesday 2nd May</span><span>7-9pm</span><span>Harbourline Hotel Parramatta Sydney. Tickets only $29.</span>
    </div>
    <a class="btn">
      <svg width="22" height="20" viewBox="0 0 24 22" aria-hidden="true"><path d="M1 1h4l3 12h12l3-9H7" stroke="#fff" stroke-width="2" fill="none"/><circle cx="10" cy="18" r="2" fill="#fff"/><circle cx="18" cy="18" r="2" fill="#fff"/></svg>
      YES - BOOK MY SEAT NOW
    </a>
    <div class="secure">**Secure Booking - Your Details are Safe!**</div>
  </div>
</section>

<section class="block instructors">
  <div class="section-title"><h2>WORKSHOP INSTRUCTORS</h2></div>
  <article class="abs instructor" style="left:73px">
    <div class="abs avatar" role="img" aria-label="Portrait of Warren Hale"></div>
    <div class="abs txt">
      <h3>Warren Hale</h3>
      <p>In 1984, at just 19 years old, I began investing in property. Over the course of the past 30 years, I've invested more than $250,000 in personal development, property seminars and programs with experts in their respective fields. Before...</p>
      <span class="read-more">Read more</span>
    </div>
  </article>
  <article class="abs instructor" style="left:619px">
    <div class="abs avatar" role="img" aria-label="Portrait of Declan Moore-Fitch"></div>
    <div class="abs txt">
      <h3>Declan Moore-Fitch</h3>
      <p>I began investing in property in 2001, when I was 25 years old. During the past 10 years, I have invested $100,000 in personal development and property seminar programs with the top people in the field of wealth creation. I consider property investment...</p>
      <span class="read-more">Read more</span>
    </div>
  </article>
  <div class="abs book-strip" style="left:0;width:1200px;top:355px">
    <small>BOOK YOUR SEAT NOW</small>
    <a class="btn">🛒 BOOK NOW -$29</a>
  </div>
</section>

<section class="block blogtest">
  <div class="abs col-head" style="left:73px;width:505px;top:20px"><h2>OUR BLOGS</h2><span class="btn-small">VIEW MORE</span></div>
  <article class="abs blog-card" style="left:73px">
    <div class="blog-img" role="img" aria-label="Video still of presenter talking to camera"></div>
    <h3>How I moved from full-time Teaching to Renovating Properties for Profit in 18 months</h3>
    <div class="meta">14/02/2017<br>by Declan Moore-Fitch</div>
    <p>Hi everyone, I'm Declan from Brickline Gains, and I thought I'd just give you a video case study of</p>
    <span class="read-more">Read more</span>
  </article>
  <article class="abs blog-card" style="left:342px">
    <div class="blog-img" role="img" aria-label="Video still of presenter inside a renovation"></div>
    <h3>7 tips to reduce risk when renovating for profit</h3>
    <div class="meta">31/01/2017<br>by Declan Moore-Fitch</div>
    <p>Hi, everyone, It's Declan from Brickline Gains and welcome to the video that's entitled, "Seven tips you need to</p>
    <span class="read-more">Read more</span>
  </article>

  <div class="abs col-head" style="left:613px;width:512px;top:20px"><h2>TESTIMONIALS</h2><span class="btn-small">VIEW MORE</span></div>
  <blockquote class="abs quote" style="top:62px;height:208px">
    <span class="qm" style="left:12px;top:10px">“</span>
    I would highly recommend people come to this event, the amount of information we have found out has been amazing! We felt very comfortable going through step by step how to renovate each phase and we were very happy with the contacts we made and the people we met.”
    <span class="qm" style="right:12px;bottom:-6px">”</span>
  </blockquote>
  <div class="abs cite" style="top:278px">- Mark &amp; Elise, 10th November Workshop</div>
  <blockquote class="abs quote" style="top:300px;height:140px">
    <span class="qm" style="left:12px;top:10px">“</span>
    Coming into the workshop it was pretty safe to say we know pretty much nothing about property. After the event we felt, especially at our age, it was definitely something that was going to set us up with a big and bright future
    <span class="qm" style="right:12px;bottom:-6px">”</span>
  </blockquote>
  <div class="abs cite" style="top:448px">- Sam &amp; Priya, 10th November Workshop</div>
</section>

<section class="block success">
  <h2>LATEST SUCCESS STORIES</h2>
  <svg class="abs arrow" style="left:50px" viewBox="0 0 40 50" aria-hidden="true"><path d="M28 8L12 25l16 17" stroke="#fff" stroke-width="6" fill="none"/></svg>
  <svg class="abs arrow" style="left:1110px" viewBox="0 0 40 50" aria-hidden="true"><path d="M12 8l16 17-16 17" stroke="#fff" stroke-width="6" fill="none"/></svg>
  <article class="abs story" style="left:92px">
    <h3>BLACKETT NSW</h3>
    <div class="story-photo" role="img" aria-label="Renovated brick house in Blackett"></div>
    <div class="story-figs"><div class="bs">BOUGHT: $220,000<br><span>SOLD: $395,000</span></div><div class="profit">$175,000<small>PROFIT</small></div></div>
  </article>
  <article class="abs story" style="left:432px">
    <h3>BLACKTOWN NSW 2148</h3>
    <div class="story-photo" role="img" aria-label="Renovated house in Blacktown"></div>
    <div class="story-figs"><div class="bs">BOUGHT: $330,000<br><span>SOLD: $395,000</span></div><div class="profit">$65,000<small>PROFIT</small></div></div>
  </article>
  <article class="abs story" style="left:772px">
    <h3>BLACKTOWN NSW 2148_2</h3>
    <div class="story-photo" role="img" aria-label="Renovated weatherboard house in Blacktown"></div>
    <div class="story-figs"><div class="bs">BOUGHT: $365,000<br><span>SOLD: $398,000</span></div><div class="profit">$33,000<small>PROFIT</small></div></div>
  </article>
</section>

<section class="block faqbooks">
  <div class="abs col-head" style="left:73px;width:513px;top:0"><h2>FREQUENTLY ASKED QUESTIONS</h2></div>
  <div class="abs faq-q" style="top:68px">Are you selling property in this workshop?<span class="tog">−</span></div>
  <p class="abs faq-a" style="top:120px">No. This is not some "buy off the plan" or "Queensland land sale" property spruiking seminar nor are we real estate agents in disguise. This is a real, live workshop with actionable take-aways and absolutely no high pressure sell or obligation to come to any other events we hold.</p>
  <div class="abs faq-q" style="top:215px">Why should I pay $29 to come to this workshop?<span class="tog">+</span></div>
  <p class="abs faq-a" style="top:270px">If you have any other questions you can always give us a call on <a>1300 555 014</a><br>or send us an email to <a>admin@bricklinegains.com.au</a></p>

  <div class="abs col-head" style="left:613px;width:512px;top:0"><h2>EBOOKS</h2><span class="btn-small">VIEW MORE</span></div>
  <div class="abs ebook" style="left:613px"><div class="ebook-cover"><div role="img" aria-label="eBook cover: 60 insider tips to add value to your property renovation" style="background:linear-gradient(180deg,#fff 0 55%,#c9a779 55%)"></div></div><div class="price">$9.97</div></div>
  <div class="abs ebook" style="left:792px"><div class="ebook-cover"><div role="img" aria-label="eBook cover: the most costly renovation mistakes" style="background:linear-gradient(180deg,#fff 0 60%,#8fae6d 60%)"></div></div><div class="price">$9.97</div></div>
  <div class="abs ebook" style="left:970px"><div class="ebook-cover"><div role="img" aria-label="eBook cover: is renovating and flipping for profit the new success story" style="background:linear-gradient(180deg,#fff 0 50%,#9ec7e0 50%)"></div></div><div class="price">$3.97</div></div>
</section>

<div class="block book-strip" style="top:3578px">
  <small>BOOK YOUR SEAT NOW</small>
  <a class="btn">🛒 BOOK NOW -$29</a>
</div>

<footer class="block site-footer">
  <div class="abs" style="left:73px;top:28px">
    <h4>QUICK LINKS</h4>
    <ul><li>Home</li><li>Our Events</li><li>Past Projects</li><li>Media eBooks</li><li>Testimonials</li><li>Blog</li><li>Contact Us</li></ul>
  </div>
  <div class="abs contact-list" style="left:235px;top:28px;width:260px">
    <h4>CONTACT US</h4>
    Harbourline Hotel Parramatta, 118 Wattle Street, Parramatta NSW 2150 (02) 5550 1827<br><br>
    Phone<br>1300 555 014<br><br>
    Email<br>admin@bricklinegains.com.au
  </div>
  <div class="abs" style="left:530px;top:28px">
    <h4>FOLLOW US</h4>
    <div class="social"><span></span><span></span><span></span><span></span></div>
  </div>
  <div class="abs book-strip" style="left:535px;top:100px;width:210px">
    <small>BOOK YOUR SEAT NOW</small>
    <a class="btn">🛒 BOOK NOW -$29</a>
  </div>
  <div class="abs news" style="left:880px;top:28px">
    <h4>GET THE NEWSLETTER</h4>
    <p>Get weekly posts and updates on<br>what we're doing.</p>
    <div class="field">Name</div>
    <div class="field">Email</div>
    <div class="sign">SIGN UP</div>
  </div>
</footer>

<div class="block copyright">© Copyright 2017 Brickline Solutions Australia. All Rights Reserved.<br>ABN 482 117 903</div>

</body>
</html>
```